Wellness IV Billboard for Naturopathic Physicians.

We need a billboard design done. We have some templates. The client would like three options to choose from. The IV bag is important this is a wellness IV billboard. The fruit needs color added. The client wants it to be obvious this is about getting a wellness IV. Same day appts available. Bright fruit is in the IV is important. You can find out more about the client at www.verdalo.clinic.

Target Market(s)

Missoula Montana

Industry/Entity Type

Health And Wellness

Font styles to use
Serif
Other font styles liked:
• see attached document with approved fonts

Colors

Designer to choose colors to be used in the design.

Requirements
Must have
• IV, logo, Wellness IVs, Same Day Appointments-See the template. Must use the graphic brand guidelines with font. Font used in template is approved to use.
Nice to have
• Must have iv bag filled with fruit and vegetables.
Should not have
• Use the attached template.

```html
<!DOCTYPE html>
<html lang="en">
<head>
<meta charset="UTF-8">
<title>Verdalo IV Therapy Billboard</title>
<link rel="stylesheet" href="https://fonts.googleapis.com/css2?family=Bitter:wght@400;500;700&family=Roboto:ital,wght@0,300;0,400;1,300&display=swap">
<style>
  :root {
    --brand-green: #5c7433;
    --ink-green: #55702d;
    --paper: #ffffff;
    --frame-grey: #8a8a8a;
    --bag-top: #f1f2ee;
    --bag-mid: #e9d9a0;
    --bag-bottom: #f2a444;
  }
  html, body {
    margin: 0;
    padding: 0;
    width: 1200px;
    height: 1200px;
    overflow: hidden;
    background: var(--paper);
  }
  .canvas {
    position: relative;
    width: 1200px;
    height: 1200px;
  }
  .billboard {
    position: absolute;
    left: 50px;
    top: 348px;
    width: 1100px;
    height: 503px;
    box-sizing: border-box;
    border: 3px solid var(--frame-grey);
    background: var(--paper);
    overflow: hidden;
  }
  .iv-bag {
    position: absolute;
    left: 810px;
    top: 6px;
    width: 272px;
    height: 482px;
    border-radius: 26px;
    background: linear-gradient(180deg, var(--bag-top) 0%, var(--bag-top) 22%, var(--bag-mid) 48%, var(--bag-bottom) 100%);
    z-index: 1;
  }
  .headline-band {
    position: absolute;
    left: 0;
    top: 0;
    width: 872px;
    height: 116px;
    z-index: 2;
  }
  .headline {
    position: absolute;
    left: 30px;
    top: 4px;
    margin: 0;
    font-family: "Bitter", serif;
    font-weight: 500;
    font-size: 110px;
    line-height: 116px;
    letter-spacing: 7px;
    color: var(--paper);
    white-space: nowrap;
    z-index: 3;
  }
  .line {
    position: absolute;
    left: 308px;
    margin: 0;
    color: var(--ink-green);
    white-space: nowrap;
  }
  .tagline {
    top: 122px;
    font-family: "Bitter", serif;
    font-weight: 700;
    font-size: 37px;
    line-height: 44px;
  }
  .same-day {
    top: 194px;
    font-family: "Bitter", serif;
    font-weight: 400;
    font-size: 30px;
    line-height: 36px;
    letter-spacing: 2.5px;
  }
  .label {
    font-family: "Roboto", sans-serif;
    font-weight: 300;
    font-style: italic;
    font-size: 29px;
    line-height: 32px;
  }
  .call-label { top: 268px; }
  .web-label { top: 381px; }
  .phone {
    top: 299px;
    font-family: "Roboto", sans-serif;
    font-weight: 400;
    font-size: 40px;
    line-height: 46px;
    letter-spacing: 5px;
  }
  .web {
    top: 415px;
    font-family: "Bitter", serif;
    font-weight: 400;
    font-size: 31px;
    line-height: 38px;
    letter-spacing: 6px;
  }
  .brand {
    position: absolute;
    left: 43px;
    top: 230px;
    width: 220px;
    text-align: center;
  }
  .brand-dot {
    display: block;
    width: 96px;
    height: 96px;
    margin: 0 auto 28px;
    border-radius: 50%;
    background: var(--brand-green);
  }
  .brand-name {
    margin: 0;
    font-family: "Bitter", serif;
    font-weight: 700;
    font-size: 42px;
    line-height: 46px;
    color: var(--brand-green);
  }
</style>
</head>
<body>
  <main class="canvas">
    <section class="billboard">
      <div class="iv-bag" role="img" aria-label="Clear IV bag filled with bright slices of lemon, orange, lime, cucumber and pepper"></div>

      <svg class="headline-band" viewBox="0 0 872 116" aria-hidden="true">
        <polygon points="0,0 805,0 872,58 805,116 0,116" fill="var(--brand-green)"/>
      </svg>
      <h1 class="headline">IV THERAPY</h1>

      <div class="brand">
        <span class="brand-dot"></span>
        <p class="brand-name">VERDALO</p>
      </div>

      <p class="line tagline">WELLNESS FROM WITH IN</p>
      <p class="line same-day">SAME DAY APPOINTMENTS</p>
      <p class="line label call-label">CALL:</p>
      <p class="line phone">406.555.0148</p>
      <p class="line label web-label">LEARN MORE AT:</p>
      <p class="line web">WWW.VERDALO.CLINIC</p>
    </section>
  </main>
</body>
</html>
```